One Pager Website for various security awareness videos

We need a one pager website (design & coding) for our security awareness video series. We imagine placing a few (3-4 sample videos) on the website, a customer referal and some contact form. SOmething similar to https://brevko.com/watch-now/. Here are some of the videos which we will place on the website:
https://www.clipvane.com/watch?v=Qa7pLm2Xw9T&t=112s
https://www.clipvane.com/watch?v=Hr4ZkeN8bVd
https://www.clipvane.com/watch?v=_9wjTPLC3KA
https://www.clipvane.com/watch?v=bvRQQsGtuHx
https://www.clipvane.com/watch?v=4yd81NkDa3p
https://www.clipvane.com/watch?v=eTWo2JsUkqC
https://www.clipvane.com/watch?v=VzPRGhd5sYo
https://www.clipvane.com/watch?v=73GkF6tWxxN
https://www.clipvane.com/watch?v=58jfZeqnK1R
As for logo: our company www.maravelguard.com is the creator of those videos. You can use our logo / name.
B2B security officers in large enterprises
1 page

```html
<!DOCTYPE html>
<html lang="en">
<head>
<meta charset="utf-8">
<title>Maravel Guard – Security Awareness Video Library</title>
<link rel="stylesheet" href="https://fonts.googleapis.com/css2?family=Figtree:wght@300;400;500;700&display=swap">
<style>
:root{
  --teal:#00b9c3;
  --orange:#fca913;
  --page:#fafafa;
  --ink:#5b5b5b;
  --ink-soft:#767676;
  --white:#ffffff;
  --line:#dcdcdc;
  --bar:#eeeeee;
  --frame:#444444;
  --placeholder:#9a9a9a;
}
*{box-sizing:border-box;margin:0;padding:0}
html,body{width:1200px;height:3163px;overflow:hidden}
body{font-family:"Figtree",sans-serif;background:var(--page);position:relative;color:var(--ink)}
a{color:inherit}

.hero{position:absolute;left:0;top:0;width:1200px;height:387px;background:var(--teal);color:var(--white)}
.brand{position:absolute;left:71px;top:52px;display:flex;align-items:center;gap:8px;font-weight:700;font-size:22px;color:#2a2a2a}
.brand-dot{width:22px;height:22px;border-radius:50%;background:var(--orange)}
.nav{position:absolute;top:50px;left:0;width:1200px;font-size:17px}
.nav a{position:absolute;text-decoration:none;color:var(--white)}
.hero-title{position:absolute;left:71px;top:172px;font-weight:400;font-size:39px;line-height:48px;letter-spacing:.5px}
.hero-sub{position:absolute;left:71px;top:270px;font-size:19px;letter-spacing:.3px}
.hero-art{position:absolute;left:766px;top:104px;width:290px;height:283px;border-radius:120px 120px 40px 60px;background:linear-gradient(140deg,#e6e9ec,#fbd0a8 60%,#e8384f)}

.video{position:absolute;width:473px}
.video-screen{height:331px;border:1.5px solid var(--frame);border-radius:3px;background:linear-gradient(180deg,#f4f4f4,#e2e2e2)}
.video-controls{margin-top:7px;height:39px;background:var(--bar);display:flex;align-items:center;padding:0 16px;gap:14px}
.video-controls .track{flex:1;height:1px;background:#c8c8c8;margin:0 6px}
.video-title{margin-top:10px;font-size:29px;font-weight:400;color:var(--ink);letter-spacing:.3px;white-space:nowrap}
.video-desc{margin-top:9px;font-size:17px;line-height:22px;font-weight:300;color:var(--ink-soft);padding-left:2px;white-space:nowrap}
.more{position:absolute;right:72px;top:1662px;font-size:20px;color:var(--teal);text-decoration:none}

.testimonial{position:absolute;left:0;top:1811px;width:1200px;height:339px;background:var(--orange)}
.testimonial-photo{position:absolute;left:130px;top:8px;width:300px;height:331px;border-radius:120px 120px 0 0;background:linear-gradient(180deg,#5a3a28 0%,#f3c560 45%,#e8b64c 100%)}
.quote{position:absolute;left:561px;top:76px;width:520px;font-size:20px;line-height:24px;color:#595959}
.quote-name{position:absolute;left:561px;top:196px;font-size:31px;color:#595959}
.quote-role{position:absolute;left:561px;top:239px;font-size:19px;color:#595959}

.contact{position:absolute;left:0;top:2150px;width:1200px;height:1013px;background:var(--teal);color:var(--white)}
.contact h2{position:absolute;left:71px;top:54px;font-size:31px;font-weight:400}
.contact-intro{position:absolute;left:71px;top:98px;font-size:17px;line-height:22px;white-space:nowrap}
.field{position:absolute;width:451px;height:49px;background:var(--white);font-size:12px;color:var(--placeholder);padding:17px 19px;letter-spacing:.3px}
.field.select::after{content:"";position:absolute;right:20px;top:21px;border-left:5px solid transparent;border-right:5px solid transparent;border-top:9px solid #222}
.field.message{width:953px;height:215px}
.submit{position:absolute;left:803px;top:2817px;width:221px;height:53px;background:var(--orange);color:#333;font-size:19px;display:flex;align-items:center;justify-content:center;letter-spacing:.5px}

.divider{position:absolute;left:71px;top:2921px;width:1057px;height:1px;background:rgba(255,255,255,.7)}
.foot-col{position:absolute;top:2950px;color:var(--white);font-size:14.5px;line-height:18.4px}
.foot-col h3{font-size:17px;font-weight:700;margin-bottom:7px;letter-spacing:.3px}
.foot-col a{display:block}
.lang{display:flex;gap:14px;align-items:center}
.lang::after{content:"";border-left:4px solid transparent;border-right:4px solid transparent;border-top:8px solid var(--white)}
.copyright{position:absolute;left:0;top:3096px;width:1200px;text-align:center;color:var(--white);font-size:14.5px}
</style>
</head>
<body>

<header class="hero">
  <div class="brand"><span class="brand-dot"></span>Maravel</div>
  <nav class="nav">
    <a href="#" style="left:592px">Home</a>
    <a href="#" style="left:744px">About</a>
    <a href="#" style="left:898px">Solution</a>
    <a href="#" style="left:1068px">Contact</a>
  </nav>
  <h1 class="hero-title">SECURITY AWARENESS<br>VIDEO LIBRARY</h1>
  <p class="hero-sub">Browse through our security awareness video series</p>
  <div class="hero-art" role="img" aria-label="Illustration of a hand holding a phone in front of video players and chat bubbles"></div>
</header>

<svg width="0" height="0" style="position:absolute">
  <defs>
    <g id="icon-play"><path d="M2 1 L12 7 L2 13 Z" fill="none" stroke="#666" stroke-width="1.4"/></g>
    <g id="icon-volume"><path d="M1 5 H4 L8 2 V12 L4 9 H1 Z" fill="none" stroke="#666" stroke-width="1.3"/><path d="M10 4.5 Q12 7 10 9.5 M11.5 3 Q14.5 7 11.5 11" fill="none" stroke="#666" stroke-width="1.1"/></g>
    <g id="icon-gear"><circle cx="7" cy="7" r="5.5" fill="none" stroke="#666" stroke-width="1.2"/><circle cx="7" cy="7" r="2" fill="none" stroke="#666" stroke-width="1.2"/></g>
    <g id="icon-full"><path d="M1 4 V1 H4 M10 1 H13 V4 M13 10 V13 H10 M4 13 H1 V10 M3 3 H11 V11 H3 Z" fill="none" stroke="#666" stroke-width="1.3"/></g>
  </defs>
</svg>

<main>
  <article class="video" style="left:71px;top:492px">
    <div class="video-screen" role="img" aria-label="Line-drawn video still of an office worker at a desk in a home office"></div>
    <div class="video-controls">
      <svg width="14" height="14"><use href="#icon-play"/></svg><span class="track"></span>
      <svg width="15" height="14"><use href="#icon-volume"/></svg><svg width="14" height="14"><use href="#icon-gear"/></svg><svg width="14" height="14"><use href="#icon-full"/></svg>
    </div>
    <h2 class="video-title">Owen Logs In From Home</h2>
    <p class="video-desc">Security awareness video about remote workplace security.<br>In this video Owen is working from home remotely and<br>learns about the security risks.</p>
  </article>

  <article class="video" style="left:656px;top:492px">
    <div class="video-screen" role="img" aria-label="Line-drawn video still of an office worker at a desk in a home office"></div>
    <div class="video-controls">
      <svg width="14" height="14"><use href="#icon-play"/></svg><span class="track"></span>
      <svg width="15" height="14"><use href="#icon-volume"/></svg><svg width="14" height="14"><use href="#icon-gear"/></svg><svg width="14" height="14"><use href="#icon-full"/></svg>
    </div>
    <h2 class="video-title">Owen Logs In From Home</h2>
    <p class="video-desc">Security awareness video about remote workplace security.<br>In this video Owen is working from home remotely and<br>learns about the security risks.</p>
  </article>

  <article class="video" style="left:71px;top:1123px">
    <div class="video-screen" role="img" aria-label="Line-drawn video still of an office worker at a desk in a home office"></div>
    <div class="video-controls">
      <svg width="14" height="14"><use href="#icon-play"/></svg><span class="track"></span>
      <svg width="15" height="14"><use href="#icon-volume"/></svg><svg width="14" height="14"><use href="#icon-gear"/></svg><svg width="14" height="14"><use href="#icon-full"/></svg>
    </div>
    <h2 class="video-title">Owen Logs In From Home</h2>
    <p class="video-desc">Security awareness video about remote workplace security.<br>In this video Owen is working from home remotely and<br>learns about the security risks.</p>
  </article>

  <article class="video" style="left:656px;top:1116px">
    <div class="video-screen" role="img" aria-label="Line-drawn video still of an office worker at a desk in a home office"></div>
    <div class="video-controls">
      <svg width="14" height="14"><use href="#icon-play"/></svg><span class="track"></span>
      <svg width="15" height="14"><use href="#icon-volume"/></svg><svg width="14" height="14"><use href="#icon-gear"/></svg><svg width="14" height="14"><use href="#icon-full"/></svg>
    </div>
    <h2 class="video-title">Owen Logs In From Home</h2>
    <p class="video-desc">Security awareness video about remote workplace security.<br>In this video Owen is working from home remotely and<br>learns about the security risks.</p>
  </article>

  <a class="more" href="#">See more videos</a>
</main>

<section class="testimonial">
  <div class="testimonial-photo" role="img" aria-label="Photo of a smiling woman in a yellow blazer holding a tablet"></div>
  <p class="quote">This explainer videos helped me learn more on security tips.The videos from maravel guard has been very vital for my organization ever since i stumbled on them. I’d recommend their services anytime!</p>
  <p class="quote-name">Nora Adeyemi</p>
  <p class="quote-role">Security Lead Harbor Line Group</p>
</section>

<section class="contact">
  <h2>Get in touch</h2>
  <p class="contact-intro">Do you have a question about our security videos or you want to know more about our<br>servics, enter your message in the form below.</p>
</section>

<div class="field" style="left:71px;top:2343px"></div>
<div class="field" style="left:575px;top:2343px">Email address*</div>
<div class="field" style="left:71px;top:2420px">Phone number</div>
<div class="field" style="left:575px;top:2420px">Company*</div>
<div class="field" style="left:71px;top:2497px">Country*</div>
<div class="field select" style="left:575px;top:2497px">How did you hear about us?</div>
<div class="field message" style="left:71px;top:2574px">Message*</div>
<div class="submit">SUBMIT</div>

<footer>
  <div class="divider"></div>
  <div class="foot-col" style="left:71px">
    <h3>CONTACT</h3>
    <p>Address: North America<br>MARAVEL Guard USA<br>4410 Larkspur Avenue<br>Suite 210<br>Denton, TX 76201</p>
  </div>
  <div class="foot-col" style="left:391px">
    <h3>CONNECT</h3>
    <a href="#">Friendnet</a><a href="#">Snapgram</a><a href="#">Chirper</a><a href="#">Clipvane</a>
  </div>
  <div class="foot-col" style="left:711px">
    <h3>INFORMATION</h3>
    <a href="#">Home</a><a href="#">About</a><a href="#">Solution</a><a href="#">Resouces</a><a href="#">Pricing</a>
  </div>
  <div class="foot-col" style="left:1031px">
    <h3>LANGUAGE</h3>
    <span class="lang">English</span>
  </div>
  <p class="copyright">© Copyright 2021. Maravel Guard. <a href="#">Privacy Policy | Terms</a></p>
</footer>

</body>
</html>
```